Wren's Hearth Support Business Card

Business card design
Font must be in Poppins Regular for Wren's Hearth Support
Safe Days Ahead font is Alex Brush

Colour must be Hex #910E2B
RGB 145-14-43
Pantone 7427 C
We want the card editable
On the front please include
Name eg Mavis Dunleavy
Position eg Clinical Care Manager
Phone number mobile 0473 856 342
Phone 08 7394 2650
Email : mavis@wrenshearthsupport.com.au
Address : Gullwing Cove, Western Australia, 6248
Website : wrenshearthsupport.com.au
Contact us today to experience the warmth, respect and personal touch of Wren's Hearth Support.

Target Market(s)

35+

Industry/Entity Type

aged care / community

Contact Information for Business Card

see project description

Requirements
Must have
• Colours, logos and fonts as detailed and uploaded

```html
<!DOCTYPE html>
<html lang="en">
<head>
<meta charset="utf-8">
<title>Wren's Hearth Support – Business Card</title>
<link rel="stylesheet" href="https://fonts.googleapis.com/css2?family=Alex+Brush&family=Poppins:wght@400;600;700&display=swap">
<style>
  :root {
    --page: #ececec;
    --card: #6c0d23;
    --leaf: rgba(150, 40, 50, 0.35);
    --cream: #ecd8c3;
    --white: #ffffff;
  }
  * { margin: 0; padding: 0; box-sizing: border-box; }
  html, body {
    width: 1024px; height: 1200px; overflow: hidden;
    background: var(--page);
    font-family: "Poppins", sans-serif;
  }
  .card {
    position: absolute; left: 115px; width: 793px;
    background: var(--card); overflow: hidden;
  }
  .card--front { top: 97px; height: 458px; }
  .card--back { top: 644px; height: 453px; }

  .foliage {
    position: absolute;
    background: radial-gradient(ellipse at center, var(--leaf) 0%, rgba(150,40,50,0) 70%);
  }
  .foliage--front-top { right: 0; top: 0; width: 190px; height: 170px; }
  .foliage--front-left { left: -20px; top: 265px; width: 110px; height: 170px; }
  .foliage--back-top { right: 0; top: 0; width: 230px; height: 150px; }
  .foliage--back-left { left: -20px; top: 300px; width: 90px; height: 150px; }

  .brand { position: absolute; left: 184px; top: 150px; display: flex; align-items: center; gap: 30px; }
  .brand__mark {
    width: 152px; height: 152px; border-radius: 50%;
    border: 11px solid var(--white); flex: none;
  }
  .brand__name {
    font-weight: 600; font-size: 38px; line-height: 40px;
    color: var(--cream); letter-spacing: -0.5px;
  }
  .brand__tagline {
    font-family: "Alex Brush", cursive;
    font-size: 34px; line-height: 40px; color: var(--white);
    margin-top: 2px;
  }

  .person { position: absolute; left: 59px; top: 74px; }
  .person__name {
    font-weight: 700; font-size: 38px; line-height: 46px;
    color: var(--cream); letter-spacing: 0.5px; text-transform: uppercase;
  }
  .person__role {
    font-size: 21px; color: var(--white); letter-spacing: 1.6px; margin-top: 8px;
  }

  .contact { position: absolute; top: 277px; font-size: 16px; line-height: 20px; color: var(--cream); }
  .contact--left { left: 59px; }
  .contact--right { left: 372px; }
  .contact__row { display: flex; gap: 20px; margin-bottom: 13px; }
  .contact__row--plain { padding-left: 36px; }
  .contact__phone { font-size: 14px; color: var(--white); }
  .contact__icon { width: 16px; height: 18px; flex: none; margin-top: 1px; fill: var(--cream); }
</style>
</head>
<body>

<section class="card card--front">
  <div class="foliage foliage--front-top" role="img" aria-label="Faint line-drawn leaf sprig"></div>
  <div class="foliage foliage--front-left" role="img" aria-label="Faint line-drawn leaf"></div>
  <div class="brand">
    <div class="brand__mark"></div>
    <div class="brand__text">
      <div class="brand__name">Wren's Hearth<br>Support</div>
      <div class="brand__tagline">Safe Days Ahead</div>
    </div>
  </div>
</section>

<section class="card card--back">
  <div class="foliage foliage--back-top" role="img" aria-label="Faint line-drawn leaf sprig"></div>
  <div class="foliage foliage--back-left" role="img" aria-label="Faint line-drawn leaf"></div>

  <div class="person">
    <h1 class="person__name">Mavis Dunleavy</h1>
    <p class="person__role">Clinical Care Manager</p>
  </div>

  <div class="contact contact--left">
    <div class="contact__row">
      <svg class="contact__icon" viewBox="0 0 16 18"><path d="M8 0a6.5 6.5 0 0 0-6.5 6.5C1.5 11 8 18 8 18s6.5-7 6.5-11.5A6.5 6.5 0 0 0 8 0zm0 9a2.5 2.5 0 1 1 0-5 2.5 2.5 0 0 1 0 5z"/></svg>
      <span>Gullwing Cove, Western<br>Australia, 6248</span>
    </div>
    <div class="contact__row">
      <svg class="contact__icon" viewBox="0 0 16 18"><path d="M3 1l3 3.5-1.6 2a10 10 0 0 0 5 5l2-1.6L15 13l-2 3c-6 0-12-6-12-12z"/></svg>
      <span class="contact__phone">0473 856 342</span>
    </div>
    <div class="contact__row contact__row--plain">
      <span class="contact__phone">08 7394 2650</span>
    </div>
  </div>

  <div class="contact contact--right">
    <div class="contact__row">
      <svg class="contact__icon" viewBox="0 0 16 18"><text x="0" y="15" font-family="Poppins, sans-serif" font-weight="700" font-size="17" fill="#ecd8c3">@</text></svg>
      <span>mavis@wrenshearthsupport.com.au</span>
    </div>
    <div class="contact__row">
      <svg class="contact__icon" viewBox="0 0 16 18"><path d="M14 3L5 6.5l3 1.3L2 14l1 1 6.2-6 1.3 3z"/></svg>
      <span>wrenshearthsupport.com.au</span>
    </div>
  </div>
</section>

</body>
</html>
```